Austin TX First Veterinary Urgent Care

We need a flyer designed for us and our clinic that is eye-catching but also summarizes the advantages of our services. We want to express that we are family owned, have convenient hours and affordable prices. We are the first veterinary urgent care animal clinic in Austin Texas. Our hours of operation are M-F 12PM-9PM S-S 10AM-6PM. Our Address is 8715 W Larkmoor Rd Suite B262 Austin, Tx 78699. Our phone number is (737)555-0148 our website is www.brolliepetco.example and our email address is info@brolliepetco.example.

Target Market(s)

Pet owners and veterinary professionals for referral purposes.

Industry/Entity Type

Veterinary

Font styles to use
Sans Serif

Colors
0094D4
00A9DD
6FCCEA
C7EBF8
E9F6FB
00AB8E
00BBA5
67D7C9
C6EFE9
E9F9F6

Requirements
Must have
• Our logo, hours of operation and contact information easy to read. Should emphasize that we are affordable as well as family owned. List of services should also be displayed: ear, eye, and skin issues, limping, broken toenails, lacerations, coughing, sneezing, allergies, vomiting and diarrhea, urinary issues, constipation, snake bites, toxin ingestion, and many many more
Nice to have
• We would like to have a modern feel with drawn/cartoon images, not realistic stock photos of dogs/cats.

```html
<!DOCTYPE html>
<html lang="en">
<head>
<meta charset="utf-8">
<title>Brollie Pet Co – Veterinary Urgent Care Flyer</title>
<link rel="stylesheet" href="https://fonts.googleapis.com/css2?family=Poppins:wght@400;500;600;700;800&display=swap">
<style>
:root{
  --navy:#0b0f86;
  --green:#3fa94a;
  --ink:#1f2330;
  --paper:#ffffff;
  --backdrop:#e7e9ee;
  --grey-icon:#9aa0a8;
}
*{margin:0;padding:0;box-sizing:border-box}
html,body{width:1200px;height:2333px;overflow:hidden;background:var(--backdrop)}
body{font-family:'Poppins',sans-serif;color:var(--ink);position:relative}
.flyer{position:absolute;left:37px;top:437px;width:804px;height:1042px;background:var(--paper);
  transform:scale(1.4);transform-origin:0 0;box-shadow:0 6px 18px rgba(0,0,0,.18);overflow:hidden}
.abs{position:absolute}
.brand{left:48px;top:58px;display:flex;align-items:center;gap:14px}
.brand-dot{width:52px;height:52px;border-radius:50%;background:var(--green)}
.brand-name{font-weight:700;font-size:40px;color:var(--navy);letter-spacing:-.5px}
.headline-1{left:48px;top:160px;font-weight:800;font-size:47px;color:var(--navy);line-height:1}
.headline-2{left:47px;top:206px;font-weight:800;font-size:60px;color:var(--green);line-height:1}
.headline-3{left:50px;top:262px;font-weight:500;font-size:39px;color:var(--navy);letter-spacing:10px;line-height:1}
.intro{left:49px;top:308px;width:380px;font-size:15.5px;line-height:1.22}
.hero-art{left:437px;top:28px;width:367px;height:334px;
  background:linear-gradient(180deg,#f0f0f2 0%,#8fa8d8 45%,#e7b85f 70%,#9a5a46 100%)}
.value{left:50px;top:378px;display:flex;gap:16px;align-items:center}
.value-text{line-height:1}
.value-text .l1{font-size:32px;font-weight:500;color:var(--navy)}
.value-text .l1 b{font-weight:700}
.value-text .l2{font-size:24px;font-weight:500;color:var(--navy);margin-top:2px}
.mini-art{top:416px;width:98px;height:88px;background:linear-gradient(180deg,#dfe9cf,#c9dcb3)}
.services-title{left:48px;top:478px;font-size:29px;font-weight:500;color:var(--navy);line-height:1}
.services-title b{font-weight:700}
.services-rule{left:47px;top:516px;width:410px;height:4px}
.services{top:540px;list-style:none}
.services li{display:flex;align-items:flex-start;gap:10px;font-size:19px;font-weight:500;line-height:23px;margin-bottom:14px}
.services li svg{flex:none;margin-top:4px}
.col-a{left:48px}
.col-b{left:278px;width:200px}
.col-divider{left:255px;top:542px;width:1px;height:285px;background:#c9ccd4}
.more{left:278px;top:808px;font-size:15px}
.door-art{left:460px;top:535px;width:305px;height:205px;
  background:linear-gradient(180deg,#c6e27a 0%,#b6d76a 55%,#e9c8a5 100%);border-radius:40px 40px 6px 6px}
.call{left:496px;top:768px;font-size:17px}
.phone-box{left:495px;top:798px;width:258px;height:104px;border:3px solid var(--green);text-align:center;background:var(--paper)}
.phone{font-size:32px;font-weight:700;color:var(--green);line-height:1;margin-top:10px;letter-spacing:.5px}
.clinic-sub{font-size:26px;line-height:1;margin-top:4px}
.clinic-main{font-size:38px;font-weight:500;line-height:1;margin-top:1px;background:var(--paper);display:inline-block;padding:0 6px;position:relative;top:2px}
.hours-rule{left:495px;top:928px;width:258px;height:2px;background:var(--navy)}
.hours{left:495px;top:934px;width:258px;height:108px;background:var(--navy);color:#fff;text-align:center;padding-top:22px;font-size:12.5px;font-weight:700;line-height:27px}
.hours span{color:#5fd36a}
.contact-bar{left:48px;top:860px;width:345px;height:28px;background:var(--green);color:#fff;font-size:14px;line-height:28px;padding-left:15px}
.contact{left:48px;top:908px;list-style:none}
.contact li{display:flex;align-items:center;gap:14px;font-size:15.5px;height:32px}
</style>
</head>
<body>
<main class="flyer">
  <div class="abs brand"><span class="brand-dot"></span><span class="brand-name">Brollie Pet Co</span></div>

  <h1>
    <span class="abs headline-1">AUSTIN TX FIRST</span>
    <span class="abs headline-2">VETERINARY</span>
    <span class="abs headline-3">URGENT CARE</span>
  </h1>
  <p class="abs intro">We are the first veterinary urgent care animal clinic in Austin Texas.</p>

  <div class="abs hero-art" role="img" aria-label="Illustration of two veterinarians examining a dog on a clinic table"></div>

  <div class="abs value">
    <svg width="62" height="62" viewBox="0 0 62 62" aria-hidden="true">
      <path d="M18 2h16v16h16v16H34v16H18V34H2V18h16z" fill="var(--grey-icon)"/>
      <circle cx="46" cy="46" r="13" fill="var(--green)" stroke="#fff" stroke-width="3"/>
      <circle cx="46" cy="49" r="4" fill="#fff"/>
      <circle cx="41" cy="43" r="2" fill="#fff"/><circle cx="46" cy="40" r="2" fill="#fff"/><circle cx="51" cy="43" r="2" fill="#fff"/>
    </svg>
    <div class="value-text">
      <div class="l1">We are <b>Affordable</b></div>
      <div class="l2">as well as family owned.</div>
    </div>
  </div>

  <div class="abs mini-art" style="left:463px" role="img" aria-label="Small illustration of a vet treating a pet"></div>
  <div class="abs mini-art" style="left:569px" role="img" aria-label="Small illustration of a family visiting the vet"></div>
  <div class="abs mini-art" style="left:675px" role="img" aria-label="Small illustration of a vet with a dog in the lab"></div>

  <h2 class="abs services-title">LIST OF <b>SERVICES</b></h2>
  <svg class="abs services-rule" viewBox="0 0 410 4" aria-hidden="true">
    <rect x="0" y="0" width="32" height="4" fill="var(--navy)"/>
    <rect x="46" y="0" width="364" height="4" fill="var(--navy)"/>
  </svg>

  <ul class="abs services col-a">
    <li><svg width="17" height="15" viewBox="0 0 17 15"><use href="#paw"/></svg>Ear</li>
    <li><svg width="17" height="15" viewBox="0 0 17 15"><use href="#paw"/></svg>Eye</li>
    <li><svg width="17" height="15" viewBox="0 0 17 15"><use href="#paw"/></svg>Skin Issues</li>
    <li><svg width="17" height="15" viewBox="0 0 17 15"><use href="#paw"/></svg>Limping</li>
    <li><svg width="17" height="15" viewBox="0 0 17 15"><use href="#paw"/></svg>Broken Toenails</li>
    <li><svg width="17" height="15" viewBox="0 0 17 15"><use href="#paw"/></svg>Lacerations</li>
    <li><svg width="17" height="15" viewBox="0 0 17 15"><use href="#paw"/></svg>Coughing</li>
    <li><svg width="17" height="15" viewBox="0 0 17 15"><use href="#paw"/></svg>Sneezing</li>
  </ul>
  <div class="abs col-divider"></div>
  <ul class="abs services col-b">
    <li><svg width="17" height="15" viewBox="0 0 17 15"><use href="#paw"/></svg>Allergies</li>
    <li><svg width="17" height="15" viewBox="0 0 17 15"><use href="#paw"/></svg>Vomiting and Diarrhea</li>
    <li><svg width="17" height="15" viewBox="0 0 17 15"><use href="#paw"/></svg>Urinary Issues</li>
    <li><svg width="17" height="15" viewBox="0 0 17 15"><use href="#paw"/></svg>Constipation</li>
    <li><svg width="17" height="15" viewBox="0 0 17 15"><use href="#paw"/></svg>Snake Bites</li>
    <li><svg width="17" height="15" viewBox="0 0 17 15"><use href="#paw"/></svg>Toxin ingestion</li>
  </ul>
  <p class="abs more">&amp; many many more......</p>

  <div class="abs door-art" role="img" aria-label="Illustration of pet owners and a vet at the clinic entrance"></div>

  <p class="abs call">Call us to make appointment</p>
  <div class="abs phone-box">
    <div class="phone">737-555-0148</div>
    <div class="clinic-sub">Animal Clinic</div>
    <div class="clinic-main">SHELTER</div>
  </div>
  <div class="abs hours-rule"></div>
  <div class="abs hours">
    MONDAY TO FRIDAY <span>12PM TO 9PM</span><br>
    SATURDAY TO SUNDAY <span>10AM TO 6PM</span>
  </div>

  <div class="abs contact-bar">CONTACT INFORMATION</div>
  <ul class="abs contact">
    <li><svg width="24" height="24" viewBox="0 0 24 24"><circle cx="12" cy="12" r="12" fill="var(--green)"/><path d="M12 5a4.5 4.5 0 0 0-4.5 4.5c0 3.3 4.5 8.5 4.5 8.5s4.5-5.2 4.5-8.5A4.5 4.5 0 0 0 12 5z" fill="#fff"/><circle cx="12" cy="9.5" r="1.7" fill="var(--green)"/></svg>8715 W Larkmoor Rd Suite B262 Austin, Tx 78699</li>
    <li><svg width="24" height="24" viewBox="0 0 24 24"><circle cx="12" cy="12" r="12" fill="var(--green)"/><rect x="6" y="8" width="12" height="9" rx="1" fill="#fff"/><path d="M6.5 8.5l5.5 4.5 5.5-4.5" fill="none" stroke="var(--green)" stroke-width="1.3"/></svg>info@brolliepetco.example</li>
    <li><svg width="24" height="24" viewBox="0 0 24 24"><circle cx="12" cy="12" r="12" fill="var(--green)"/><g fill="none" stroke="#fff" stroke-width="1.3"><circle cx="12" cy="12" r="6"/><ellipse cx="12" cy="12" rx="2.6" ry="6"/><path d="M6 12h12M7 9h10M7 15h10"/></g></svg>www.brolliepetco.example</li>
  </ul>

  <svg width="0" height="0" style="position:absolute" aria-hidden="true">
    <defs>
      <g id="paw" fill="var(--grey-icon)">
        <ellipse cx="8.5" cy="10.5" rx="4" ry="3.5"/>
        <circle cx="2.5" cy="6.5" r="1.8"/><circle cx="6" cy="3" r="1.8"/>
        <circle cx="11" cy="3" r="1.8"/><circle cx="14.5" cy="6.5" r="1.8"/>
      </g>
    </defs>
  </svg>
</main>
</body>
</html>
```